■デザインへの要望
1)フライヤーのイメージとしては明るく女性的なイメージを希望します。
2)人物写真は使わないでください。
3)コーポレートロゴを右上に配置してください。
ロゴの改変(色の変更や比率の変更)はご遠慮ください。
4)会のロゴを配置してください。
位置はお任せしますが、サイズの変更はご遠慮ください。
※前回のフライヤーを素材と一緒にお付けしますのでご参考になさってください。

■素材
1)フライヤーを作成する際に必要なロゴ等の画像等は

```html
<!DOCTYPE html>
<html lang="ja">
<head>
<meta charset="utf-8">
<title>ランチョンセミナー15</title>
<link rel="stylesheet" href="https://fonts.googleapis.com/css2?family=Noto+Sans+JP:wght@400;500;700;900&family=Noto+Serif+JP:wght@400;600;700;900&display=swap">
<style>
:root{
  --green:#3f9a2c;
  --green-dark:#2d7a1f;
  --green-light:#9ccc3c;
  --ink:#1a1a1a;
  --grey:#555;
}
*{margin:0;padding:0;box-sizing:border-box}
html,body{width:846px;height:1200px;overflow:hidden}
body{font-family:"Noto Sans JP",sans-serif;color:var(--ink);background:#fff}
.flyer{position:relative;width:846px;height:1200px;overflow:hidden;background:#fff}
.lower-band{position:absolute;left:0;top:560px;width:846px;height:640px}
.brand{position:absolute;right:36px;top:70px;display:flex;align-items:center;gap:10px;
  font-weight:700;font-size:30px;line-height:1;color:var(--green)}
.brand .dot{width:24px;height:24px;border-radius:50%;background:var(--green)}
.society{position:absolute;left:0;right:0;top:100px;text-align:center;line-height:1}
.society .mark{display:inline-flex;align-items:center;gap:6px;font-weight:700;font-size:14px;color:var(--green-dark)}
.society .mark i{width:10px;height:10px;border-radius:50%;background:var(--green)}
.society .name{font-family:"Noto Serif JP",serif;font-size:24px;font-weight:600;margin-top:12px}
.seminar{position:absolute;left:0;right:0;top:180px;text-align:center;line-height:1}
.seminar span{display:inline-block;padding:6px 30px;font-size:28px;font-weight:700;color:var(--green);
  border-top:2px solid var(--green-light);border-bottom:2px solid var(--green-light)}
.title{position:absolute;left:0;right:0;text-align:center;font-family:"Noto Serif JP",serif;font-weight:900;line-height:1;color:var(--ink);white-space:nowrap}
.t1{top:236px;font-size:52px}
.t2{top:312px;font-size:76px}
.t2 .u{background:linear-gradient(transparent 80%,var(--green-light) 80%)}
.t3{top:412px;font-size:58px}
.subtitle{position:absolute;left:140px;right:140px;top:490px;text-align:center;font-size:24px;font-weight:700;line-height:1;
  color:var(--green);border-top:2px solid var(--green-light);border-bottom:2px solid var(--green-light);padding:8px 0}
.english{position:absolute;left:0;right:0;top:552px;text-align:center;font-family:"Noto Serif JP",serif;font-size:20px;line-height:1;color:var(--grey)}
.date{position:absolute;left:0;right:0;top:656px;text-align:center;font-weight:900;font-size:46px;line-height:1;white-space:nowrap}
.date .dow{display:inline-block;width:34px;height:34px;line-height:34px;border-radius:50%;background:var(--ink);color:#fff;font-size:22px;vertical-align:6px;margin:0 6px}
.venue{position:absolute;left:0;right:0;top:716px;text-align:center;font-size:24px;font-weight:700;line-height:1}
.venue small{font-size:18px;font-weight:500}
.person{position:absolute;left:280px;display:flex;gap:18px;align-items:flex-start}
.role{width:62px;height:62px;background:var(--green);color:#fff;font-family:"Noto Serif JP",serif;font-weight:700;font-size:26px;
  display:flex;align-items:center;justify-content:center;border-radius:4px}
.pname{font-family:"Noto Serif JP",serif;font-size:42px;font-weight:900;line-height:1.1}
.pname small{font-size:22px;font-weight:700}
.aff{font-size:12px;color:var(--grey);line-height:1.5;margin-top:4px}
.chair{top:780px}
.speaker{top:880px}
.footer{position:absolute;left:0;right:0;top:1080px;text-align:center;font-family:"Noto Serif JP",serif;font-size:14px;color:var(--grey);line-height:1.6}
</style>
</head>
<body>
<div class="flyer">
  <svg class="lower-band" viewBox="0 0 846 640" aria-hidden="true">
    <defs>
      <linearGradient id="wash" x1="0" y1="0" x2="0" y2="1">
        <stop offset="0" stop-color="#eef6c4"/>
        <stop offset="1" stop-color="#dcee9a"/>
      </linearGradient>
    </defs>
    <path d="M0 40 C220 0 620 70 846 20 V640 H0 Z" fill="url(#wash)"/>
    <path d="M0 55 C240 15 600 90 846 38" fill="none" stroke="#9ccc3c" stroke-width="3"/>
    <path d="M0 590 C260 550 580 630 846 580 V640 H0 Z" fill="#c7e27a"/>
  </svg>

  <div class="brand"><span class="dot"></span>ミドリケア</div>

  <div class="society">
    <div class="mark"><i></i>嚥下ケア学会</div>
    <div class="name">第25回日本嚥下ケア研究学会学術大会</div>
  </div>

  <div class="seminar"><span>ランチョンセミナー15</span></div>

  <h1 class="title t1">これからの</h1>
  <div class="title t2"><span class="u">摂食嚥下障害看護に</span></div>
  <div class="title t3">何が求められているか</div>

  <div class="subtitle">〜「機能低下予防」と「終末期care」〜</div>
  <div class="english">What is required in the future for dysphagia nursing</div>

  <div class="date">2019年9月7日<span class="dow">土</span>12:00～13:00</div>
  <div class="venue">第8会場 <small>(港メッセ 北浜コンベンションセンター 2F 中会議室 201)</small></div>

  <div class="person chair">
    <div class="role">座長</div>
    <div>
      <div class="pname">森川 春香 <small>先生</small></div>
      <div class="aff">瀬戸内看護大学<br>名誉教授</div>
    </div>
  </div>

  <div class="person speaker">
    <div class="role">演者</div>
    <div>
      <div class="pname">高野 由紀 <small>先生</small></div>
      <div class="aff">北浜中央病院 看護部 摂食嚥下障害看護認定看護師<br>同 看護研修センター 主任教員</div>
    </div>
  </div>

  <div class="footer">【共催】<br>第25回日本嚥下ケア研究学会学術大会<br>ミドリケア株式会社</div>
</div>
</body>
</html>
```